Business card design for new, innovative company - BluePlinth

We are a new company looking for a business card design that is fun, different and quirky. Must use corporate colour green - CMYK C:55, M:0, Y:100, K:0, and corporate colour grey - C:0, M:0, Y: 0, K:70.

We have developed the first real time data application, in which people are able to profile the data of their existing customers in order to pull out more good fit clients to direct their marketing activities at.

Industry/Entity Type

Marketing

Requirements
Must have
• Logo, name, title, telephone number, fax number, email, website, address

```html
<!DOCTYPE html>
<html lang="en">
<head>
<meta charset="utf-8">
<title>BluePlinth Business Card</title>
<link rel="stylesheet" href="https://fonts.googleapis.com/css2?family=Roboto+Condensed:wght@400;700&display=swap">
<style>
  :root {
    --brand-green: #7dc242;
    --brand-grey: #6d6e70;
    --card-white: #ffffff;
    --stage: #e9e9e7;
    --text-light: #ffffff;
  }
  * { box-sizing: border-box; margin: 0; padding: 0; }
  html, body {
    width: 1200px;
    height: 901px;
    overflow: hidden;
  }
  body {
    background: var(--stage);
    font-family: "Roboto Condensed", "Arial Narrow", sans-serif;
    position: relative;
  }
  .card {
    position: absolute;
    top: 290px;
    width: 520px;
    height: 320px;
    box-shadow: 0 6px 18px rgba(0, 0, 0, 0.18);
    overflow: hidden;
  }
  .card-front {
    left: 60px;
    background: var(--card-white);
    display: flex;
    align-items: center;
    justify-content: center;
    gap: 12px;
  }
  .brand-mark {
    width: 26px;
    height: 26px;
    background: var(--brand-green);
  }
  .brand-name {
    font-weight: 700;
    font-size: 52px;
    letter-spacing: -0.5px;
    color: var(--brand-grey);
    line-height: 1;
  }
  .card-back {
    left: 620px;
    background: var(--brand-grey);
  }
  .contact {
    position: absolute;
    left: 24px;
    top: 126px;
    color: var(--text-light);
    font-size: 13px;
    line-height: 18px;
  }
  .contact-name {
    color: var(--brand-green);
    font-weight: 700;
    font-size: 17px;
    line-height: 20px;
    margin-bottom: 16px;
  }
  .contact-group { margin-bottom: 16px; }
  .contact-group:last-child { margin-bottom: 0; }
  .accent-square {
    position: absolute;
    right: 40px;
    top: 60px;
    width: 180px;
    height: 180px;
    background: var(--brand-green);
  }
</style>
</head>
<body>
  <section class="card card-front" aria-label="Card front">
    <span class="brand-mark" aria-hidden="true"></span>
    <span class="brand-name">BluePlinth</span>
  </section>

  <section class="card card-back" aria-label="Card back">
    <div class="accent-square" aria-hidden="true"></div>
    <div class="contact">
      <p class="contact-name">Nadia Fenwick</p>
      <div class="contact-group">
        <p>m. 07700 918 442</p>
        <p>t. 01632 960 517</p>
      </div>
      <div class="contact-group">
        <p>22 Willowmere Road, Ely</p>
        <p>Cambridgeshire, CB7 4QZ</p>
      </div>
      <div class="contact-group">
        <p>www.blueplinth.com</p>
        <p>nadia.fenwick@blueplinth.com</p>
      </div>
    </div>
  </section>
</body>
</html>
```